Pool Services Flyer promote regular pool services

We need a flyer design to be send out as a DL Postcard

We are a pool and spa maintenance business and would like to promote of regular pool services.
Please see our website www.bluetidepoolcare.com.au and our facebook page https://www.facebook.com/pages/Brightwater-Pools-N-Spas/418275390162847

We are pretty flexible with layouts etc Our monthly pool service is $67.00 plus chemicals so we would like this highlighted on our ad. We also so one off, weekly and fortnightly services as well.

We would like our details and logo on front and website also listed.

Target Market(s)

Pool owners

Industry/Entity Type

Pool Service

Colors
33a6d7
0292cd
0555a3
3276b5
85abd2

Requirements
Must have
• Logo
• website address
• phone number
• Price
• Promote the fact that customer wont have to worry about their pool
Nice to have
• like to have a blue wave down the bottom of flyer witht eh contact information in it. Would like to to be crisp not over crowed with information

```html
<!DOCTYPE html>
<html lang="en">
<head>
<meta charset="utf-8">
<title>Bluetide Pool Care – DL Postcard</title>
<link rel="stylesheet" href="https://fonts.googleapis.com/css2?family=Arimo:wght@400;700&family=Days+One&display=swap">
<style>
  :root {
    --sky: #33a6d7;
    --azure: #0292cd;
    --navy: #0555a3;
    --mid-blue: #3276b5;
    --pale-blue: #85abd2;
    --deep-navy: #0a2f5c;
    --ink: #0d1b33;
    --white: #ffffff;
    --backdrop: #2a2a2a;
  }
  * { margin: 0; padding: 0; box-sizing: border-box; }
  html, body { width: 928px; height: 1200px; overflow: hidden; }
  body {
    background: var(--backdrop);
    font-family: "Arimo", Arial, sans-serif;
    position: relative;
  }
  .postcard {
    position: absolute;
    left: 24px; top: 378px;
    width: 880px; height: 443px;
    overflow: hidden;
    background: var(--white);
  }
  .postcard-art { position: absolute; inset: 0; }
  .brand {
    position: absolute;
    left: 22px; top: 40px;
    width: 150px;
    text-align: center;
  }
  .brand-dot {
    width: 46px; height: 46px;
    border-radius: 50%;
    background: var(--sky);
    margin: 0 auto 10px;
  }
  .brand-name {
    font-size: 18px;
    font-weight: 400;
    color: var(--ink);
    line-height: 1.15;
  }
  .headline {
    position: absolute;
    left: 160px; top: 30px;
    font-family: "Days One", "Arial Black", sans-serif;
    font-style: italic;
    font-size: 27px;
    line-height: 1.02;
    color: var(--white);
    text-align: center;
    letter-spacing: 0.3px;
    -webkit-text-stroke: 1.2px var(--navy);
    text-shadow: 2px 2px 0 var(--navy);
  }
  .pitch {
    position: absolute;
    left: 154px; top: 120px;
    font-weight: 700;
    font-size: 16px;
    line-height: 1.2;
    color: var(--ink);
  }
  .service-list {
    position: absolute;
    left: 154px; top: 165px;
    list-style: none;
    font-size: 17px;
    line-height: 20.5px;
    color: var(--white);
  }
  .service-list li::before {
    content: "";
    display: inline-block;
    width: 8px; height: 8px;
    border-radius: 50%;
    background: var(--white);
    margin-right: 4px;
    vertical-align: 2px;
  }
  .price-badge {
    position: absolute;
    left: 19px; top: 316px;
    width: 112px; height: 112px;
    border-radius: 50%;
    background: radial-gradient(circle at 40% 35%, var(--sky), var(--azure) 70%);
    border: 5px solid var(--white);
    box-shadow: 0 0 0 3px var(--azure);
    display: flex; align-items: center; justify-content: center;
    text-align: center;
    font-family: "Days One", "Arial Black", sans-serif;
    font-style: italic;
    color: var(--white);
    font-size: 15px;
    line-height: 1.05;
    -webkit-text-stroke: 0.6px var(--navy);
  }
  .contact {
    position: absolute;
    left: 653px; top: 322px;
    font-weight: 700;
    font-size: 21px;
    color: var(--deep-navy);
  }
  .contact-line { display: flex; align-items: center; gap: 6px; height: 35px; }
  .contact-line svg { width: 22px; height: 22px; }
  .website {
    position: absolute;
    right: 30px; top: 394px;
    font-weight: 700;
    font-size: 20px;
    color: var(--deep-navy);
  }
</style>
</head>
<body>
  <main class="postcard">
    <svg class="postcard-art" viewBox="0 0 880 443" width="880" height="443" aria-hidden="false">
      <defs>
        <linearGradient id="waterGradient" x1="0" y1="0" x2="0" y2="1">
          <stop offset="0" stop-color="#ffffff"/>
          <stop offset="0.22" stop-color="#bfe2f3"/>
          <stop offset="0.45" stop-color="#33a6d7"/>
          <stop offset="0.8" stop-color="#0292cd"/>
          <stop offset="1" stop-color="#0555a3"/>
        </linearGradient>
        <linearGradient id="poolGradient" x1="0" y1="0" x2="1" y2="1">
          <stop offset="0" stop-color="#7fd3ea"/>
          <stop offset="0.5" stop-color="#4fbfe0"/>
          <stop offset="1" stop-color="#2aa3cf"/>
        </linearGradient>
      </defs>
      <rect class="water-field" width="880" height="443" fill="url(#waterGradient)"/>
      <path class="photo-frame" d="M560 0 C 525 110, 555 230, 640 300 L880 300 L880 0 Z" fill="#ffffff"/>
      <path class="swimmer-photo" role="img" aria-label="Photo of a woman swimming in clear blue pool water"
            d="M575 0 C 543 110, 570 225, 650 290 L880 290 L880 0 Z" fill="url(#poolGradient)"/>
      <path class="wave-stripe" d="M0 395 C 220 410, 420 300, 620 292 C 740 287, 820 292, 880 298 L880 318 C 760 305, 640 305, 520 330 C 360 365, 200 430, 0 420 Z" fill="#0555a3"/>
      <path class="wave-stripe-light" d="M0 380 C 230 395, 430 285, 640 278 C 760 275, 830 282, 880 288 L880 296 C 820 290, 740 286, 620 290 C 420 298, 220 405, 0 392 Z" fill="#85abd2"/>
      <path class="contact-wave" d="M0 443 L0 432 C 220 440, 380 360, 540 325 C 670 300, 790 305, 880 312 L880 443 Z" fill="#ffffff"/>
    </svg>

    <div class="brand">
      <div class="brand-dot"></div>
      <div class="brand-name">Bluetide Pool Care</div>
    </div>

    <h1 class="headline">"For All Your Cleaning &amp;<br>&nbsp;&nbsp;&nbsp;&nbsp;&nbsp;Maintenance Needs"</h1>

    <p class="pitch">Can't Seem To Get Your Pool Quite Right?<br>or Just Don't Have The Time?</p>

    <ul class="service-list">
      <li>Pool Resurfacing</li>
      <li>2-pack Epoxy or Chlorinated Rubber</li>
      <li>One-off, Weekly or Monthly Service Available</li>
      <li>Sand Changes</li>
      <li>Chemicals</li>
      <li>Installation of Pumps &amp; Piping</li>
    </ul>

    <div class="price-badge">$67.00<br>plus<br>chemicals</div>

    <div class="contact">
      <div class="contact-line">
        <svg viewBox="0 0 24 24" aria-hidden="true"><rect x="2" y="5" width="20" height="15" rx="3" fill="none" stroke="#0a2f5c" stroke-width="2"/><rect x="6" y="9" width="12" height="3" fill="#0a2f5c"/><rect x="6" y="14" width="12" height="2" fill="#0a2f5c"/></svg>
        <span>(02) 4955 0187</span>
      </div>
      <div class="contact-line">
        <svg viewBox="0 0 24 24" aria-hidden="true"><rect x="5" y="2" width="14" height="20" rx="3" fill="none" stroke="#0a2f5c" stroke-width="2"/><circle cx="12" cy="18" r="1.3" fill="#0a2f5c"/></svg>
        <span>0400 555 318</span>
      </div>
    </div>

    <div class="website">www.bluetidepoolcare.com.au</div>
  </main>
</body>
</html>
```